Kereru Creative Food Fiesta

We are holding our inaugural event on the 21st October 2022 on the FieldSolve campus in Palmerston North., from 10am until 2pm.The event will be a mix of Fourth year Food Technology students presenting their student projects and local producers show casing and educating around their products. The event is bought to you by CropNest along with Tarrowby Vale District Council and RIVO. The overall plan is to bring a spotlight to the amount of research and food related businesses are on this side of the river. The event will be free to enter and there will be food and products to purchase, but the main focus is on education.

```html
<!DOCTYPE html>
<html lang="en">
<head>
<meta charset="utf-8">
<title>Kereru Creative Food Fiesta</title>
<link rel="stylesheet" href="https://fonts.googleapis.com/css2?family=Montserrat:wght@300;400;600;700;800&family=Luckiest+Guy&display=swap">
<style>
  :root {
    --page: #ffffff;
    --frame: #d4d4d4;
    --sky-top: #1e9fe6;
    --sky-mid: #7cc9f0;
    --haze: #cfe7f2;
    --grass: #3fa43a;
    --grass-light: #7fcf4a;
    --panel-top: #43c9bd;
    --panel-bottom: #6fd57f;
    --white: #ffffff;
    --yellow: #f5f02a;
    --ring: #2d9be0;
    --label: #6fd6fb;
    --label-edge: #0f4a78;
  }
  * { margin: 0; padding: 0; box-sizing: border-box; }
  html, body { width: 1200px; height: 1072px; overflow: hidden; background: var(--page); }
  body { position: relative; font-family: "Montserrat", Arial, sans-serif; }

  .presentation-frame {
    position: absolute; left: 18px; top: 18px; width: 1164px; height: 1036px;
    border: 1px solid var(--frame);
  }

  .poster {
    position: absolute; left: 285px; top: 127px; width: 594px; height: 766px;
    overflow: hidden; color: var(--white);
  }
  .poster-backdrop {
    position: absolute; inset: 0;
    background: linear-gradient(180deg, var(--sky-top) 0%, var(--sky-mid) 38%, var(--haze) 55%, #9fb7c2 62%, var(--grass-light) 78%, var(--grass) 100%);
  }

  .title-panel {
    position: absolute; left: 67px; top: 0; width: 261px; height: 413px;
    border-radius: 0 0 46px 46px;
    background: linear-gradient(180deg, var(--panel-top), var(--panel-bottom));
    text-align: center;
  }
  .title-light { position: absolute; left: 0; right: 0; font-weight: 400; font-size: 28px; letter-spacing: 0.5px; }
  .title-bold { position: absolute; left: 0; right: 0; font-weight: 800; font-size: 44px; }
  .event-date { position: absolute; left: 0; right: 0; top: 256px; font-weight: 700; font-size: 20px; }
  .event-date sup { font-size: 11px; }
  .yellow { color: var(--yellow); }
  .event-time {
    position: absolute; left: 29px; right: 29px; top: 288px; height: 26px;
    border-top: 1.5px solid var(--white); border-bottom: 1.5px solid var(--white);
    font-weight: 700; font-size: 15px; line-height: 23px;
  }
  .event-time .divider { display: inline-block; width: 1.5px; height: 16px; background: var(--white); vertical-align: -3px; margin: 0 6px; }
  .venue-label { position: absolute; left: 0; right: 0; top: 328px; font-weight: 800; font-size: 14px; color: var(--yellow); }
  .venue-line { position: absolute; left: 0; right: 0; font-weight: 700; font-size: 18px; }

  .purpose {
    position: absolute; left: 340px; top: 38px; width: 250px; text-align: center;
    font-weight: 700; font-size: 11.2px; line-height: 15px;
  }
  .purpose h2 { font-size: 15px; font-weight: 800; letter-spacing: 0.5px; margin-bottom: 20px; }
  .purpose p + p { margin-top: 14px; }

  .sponsor-heading {
    position: absolute; left: 0; width: 602px; top: 434px; text-align: center;
    font-size: 10px; font-weight: 800; color: var(--yellow); letter-spacing: 0.3px;
  }
  .sponsor-row { position: absolute; top: 455px; left: 0; width: 594px; height: 34px; }
  .sponsor-name { position: absolute; top: 0; font-weight: 700; font-size: 20px; line-height: 34px; color: var(--white); }
  .sponsor-sep { position: absolute; top: 2px; width: 2px; height: 30px; background: var(--white); }

  .feature-photo {
    position: absolute; width: 156px; height: 156px; border-radius: 50%;
    border: 4px solid var(--white); box-shadow: 0 0 0 4px var(--ring);
  }
  .photo-students { left: 45px; top: 522px; background: radial-gradient(circle at 45% 50%, #6c8fb5, #c9b39b 55%, #7c6a58); }
  .photo-chef { left: 219px; top: 522px; background: radial-gradient(circle at 50% 45%, #f4f4f4, #d7dde2 60%, #b9c8d2); }
  .photo-trucks { left: 397px; top: 522px; background: radial-gradient(circle at 45% 60%, #f2c12e, #e6a32a 45%, #6ea84f 80%); }

  .feature-label {
    position: absolute; width: 170px; text-align: center; top: 700px;
    font-family: "Luckiest Guy", "Arial Black", sans-serif; font-size: 18px; line-height: 24px; letter-spacing: 0.5px;
    color: var(--label);
    text-shadow: -1.5px -1.5px 0 var(--label-edge), 1.5px -1.5px 0 var(--label-edge), -1.5px 1.5px 0 var(--label-edge), 1.5px 1.5px 0 var(--label-edge);
  }
</style>
</head>
<body>
  <div class="presentation-frame"></div>

  <main class="poster">
    <div class="poster-backdrop" role="img" aria-label="Photo of a pedestrian bridge over a river under a blue sky with trees and green grass"></div>

    <section class="title-panel">
      <div class="title-light" style="top:36px">KERERU</div>
      <div class="title-light" style="top:80px">CREATIVE</div>
      <div class="title-bold" style="top:122px">FOOD</div>
      <div class="title-bold" style="top:182px">FIESTA</div>
      <div class="event-date"><span class="yellow">21<sup>st</sup></span> OCTOBER <span class="yellow">2022</span></div>
      <div class="event-time"><span class="yellow">TIME</span><span class="divider"></span>At Sharp <span class="yellow">10:00</span> AM</div>
      <div class="venue-label">VENUE</div>
      <div class="venue-line" style="top:350px">FieldSolve Campus</div>
      <div class="venue-line" style="top:374px">In Palmerston North</div>
    </section>

    <section class="purpose">
      <h2>PURPOSE</h2>
      <p>Fourth year Food Technology students presenting projects &amp; local producers show casing and educating around their products.</p>
      <p>The overall plan is to bring a spotlight to the amount of research and food related businesses are on this side of the river. The event will be free to enter and there will be food &amp; products to purchase, but the main focus is on education.</p>
    </section>

    <div class="sponsor-heading">THE EVENT IS BROUGHT TO YOU BY</div>
    <div class="sponsor-row">
      <span class="sponsor-name" style="left:70px">CropNest</span>
      <span class="sponsor-sep" style="left:178px"></span>
      <span class="sponsor-name" style="left:192px;font-size:16px">TARROWBY VALE</span>
      <span class="sponsor-sep" style="left:348px"></span>
      <span class="sponsor-name" style="left:398px">RIVO</span>
    </div>

    <div class="feature-photo photo-students" role="img" aria-label="Photo of students working on a food project"></div>
    <div class="feature-photo photo-chef" role="img" aria-label="Photo of a chef in white uniform"></div>
    <div class="feature-photo photo-trucks" role="img" aria-label="Photo of colourful food trucks"></div>

    <div class="feature-label" style="left:38px">STUDENT'S<br>PROJECTS</div>
    <div class="feature-label" style="left:212px">CHEF'S<br>DEMONSTRATION</div>
    <div class="feature-label" style="left:390px">FOOD TRUCKS<br>FOR LUNCH</div>
  </main>
</body>
</html>
```